Container for chopstick set. Box or cylinder

The package will hold 5 pairs of black chopsticks (see uploaded file). These are the things that we liked from the attached files:
Idea 1: Kraft paper, illustration, the contrast of the green color with black illustration + text and green background
Idea 2: cylinder
Idea 3: Illustration of product, slide opening box type

Target Market(s)

The target market are women with families around between the ages of 25-50.

Font styles to use
Other font styles liked:
• Please see logo

Colors

Designer to choose colors to be used in the design.

Requirements
Must have
• Please incorporate our logo into the package (it's ok to change the colors of our logo), but our logo shouldn't cover a significant surface of the package
• Be creative with color(s).
Nice to have
• Possible designs:
• 1) Cylinder (4cm diameter, 25cm height)
• Alternative A: black matte background
• Alternative B: similar colors in Idea 1 with Kraft paper background.
• 2) Slide opening box (7cm x 25cm x 1cm)
• Alternative C: white box which incorporates our green logo (bottom right)

```html
<!DOCTYPE html>
<html lang="en">
<head>
<meta charset="UTF-8">
<title>Sorellia Chopstick Box – Front Panel</title>
<link rel="stylesheet" href="https://fonts.googleapis.com/css2?family=Lato:wght@400;700&display=swap">
<style>
  :root {
    --page-bg: #f4f4f6;
    --panel-black: #231f20;
    --gold-deep: #8c4526;
    --gold-amber: #c27a2c;
    --gold-bright: #e3a93b;
    --gold-light: #f6d985;
    --blossom-gold: rgba(240, 200, 110, 0.42);
    --blossom-amber: rgba(214, 160, 80, 0.36);
    --brand-green: #b4d977;
    --label-ink: #1c1a1a;
    --brand-ink: #ffffff;
  }
  html, body {
    margin: 0;
    padding: 0;
    width: 964px;
    height: 1200px;
    overflow: hidden;
    background: var(--page-bg);
  }
  .canvas {
    position: relative;
    width: 964px;
    height: 1200px;
  }
  .blossom-pattern {
    position: absolute;
    left: 340px;
    top: 272px;
    width: 283px;
    height: 834px;
    background:
      radial-gradient(ellipse 120px 90px at 40px 60px, var(--blossom-gold), transparent 70%),
      radial-gradient(ellipse 140px 110px at 150px 200px, var(--blossom-amber), transparent 70%),
      radial-gradient(ellipse 120px 100px at 250px 90px, var(--blossom-gold), transparent 70%),
      radial-gradient(ellipse 130px 120px at 260px 360px, var(--blossom-gold), transparent 70%),
      radial-gradient(ellipse 110px 130px at 40px 430px, var(--blossom-amber), transparent 70%),
      radial-gradient(ellipse 120px 120px at 260px 600px, var(--blossom-gold), transparent 70%),
      radial-gradient(ellipse 110px 140px at 50px 700px, var(--blossom-amber), transparent 70%),
      radial-gradient(ellipse 120px 100px at 250px 790px, var(--blossom-gold), transparent 70%),
      var(--panel-black);
  }
  .box-front {
    position: absolute;
    left: 0;
    top: 0;
    display: block;
  }
  .brand-name {
    font-family: "Lato", sans-serif;
    font-weight: 700;
    font-size: 31px;
    fill: var(--brand-ink);
    letter-spacing: 0.5px;
  }
  .product-label {
    font-family: "Lato", sans-serif;
    font-weight: 700;
    font-size: 33px;
    fill: var(--label-ink);
    letter-spacing: 0.6px;
  }
</style>
</head>
<body>
<main class="canvas">
  <div class="blossom-pattern" role="img" aria-label="Gold plum blossom branches pattern on black"></div>
  <svg class="box-front" width="964" height="1200" viewBox="0 0 964 1200" xmlns="http://www.w3.org/2000/svg">
    <defs>
      <linearGradient id="gold-foil" x1="0" y1="0" x2="1" y2="0">
        <stop offset="0" stop-color="#c27a2c"/>
        <stop offset="0.25" stop-color="#e3a93b"/>
        <stop offset="0.5" stop-color="#f6d985"/>
        <stop offset="0.75" stop-color="#c27a2c"/>
        <stop offset="1" stop-color="#8c4526"/>
      </linearGradient>
    </defs>

    <rect class="header-band" x="340" y="94" width="283" height="178" fill="url(#gold-foil)"/>
    <circle class="brand-dot" cx="481" cy="166" r="31" fill="#b4d977"/>
    <text class="brand-name" x="481" y="246" text-anchor="middle">sorellia</text>

    <path class="label-tab" d="M438 1106 V545 A43.5 43.5 0 0 1 525 545 V1106 Z" fill="url(#gold-foil)"/>
    <text class="product-label" transform="translate(493 1072) rotate(-90)" x="0" y="0" textLength="526" lengthAdjust="spacingAndGlyphs">5 PAIRS OF BLACK CHOPSTICKS</text>
  </svg>
</main>
</body>
</html>
```